Professional Services - letterhead / business cards

The company (velmora holdings) will provide services to Investment Funds and large investors in Spain. I have recently chosen a logo that I am attaching.

I would like a simple stationary design that i could use as letter head, business cards and "with compliments" cards.

I am not quite sure which color I will mostly use for the logo, in the email signature I will probably lean towards the white background and grey letters. I am attaching my favourite options.

Target Market(s)

Large Multinationals, Investment funds and Law firms

Industry/Entity Type

Business

Requirements
Must have
• my details are:
Luis R. Albarda
Velmora Holdings S.L.
Casa de Valdetorres
Calle de Ortuzar Beltrán 27
28019 Madrid
T: +34 (91) 387-6051
M: +34 (655) 814-073
e-mail: lalbarda@velmoraholdings.example

```html
<!DOCTYPE html>
<html lang="en">
<head>
<meta charset="utf-8">
<title>Velmora Holdings – Business Card</title>
<link rel="stylesheet" href="https://fonts.googleapis.com/css2?family=Questrial&display=swap">
<style>
  :root {
    --navy: #2b2c6e;
    --navy-light: #55599a;
    --paper: #f3f3f3;
    --ink-grey: #6b6b70;
    --backdrop: #d9d9d9;
    --font: "Questrial", "Century Gothic", sans-serif;
  }
  * { box-sizing: border-box; margin: 0; padding: 0; }
  html, body { width: 1200px; height: 900px; overflow: hidden; }
  body {
    background: var(--backdrop);
    font-family: var(--font);
    position: relative;
  }
  .card {
    position: absolute;
    left: 320px;
    width: 560px;
    height: 340px;
    border-radius: 2px;
    overflow: hidden;
  }
  .card--front {
    top: 60px;
    background: radial-gradient(ellipse at 70% 90%, var(--navy-light) 0%, var(--navy) 75%);
    display: flex;
    align-items: center;
    justify-content: center;
  }
  .card--front .wordmark {
    color: #ffffff;
    font-size: 34px;
    letter-spacing: 0.5px;
  }
  .card--back {
    top: 480px;
    background: var(--paper);
  }
  .card--back .wordmark {
    position: absolute;
    left: 34px;
    top: 96px;
    color: var(--navy);
    font-size: 30px;
  }
  .holder-tab {
    position: absolute;
    right: 0;
    top: 54px;
    width: 16px;
    height: 38px;
    background: var(--navy);
    border-radius: 19px 0 0 19px;
  }
  .holder-name {
    position: absolute;
    right: 34px;
    top: 60px;
    color: var(--navy);
    font-size: 19px;
    font-weight: 400;
  }
  .company-address {
    position: absolute;
    left: 34px;
    top: 170px;
    font-style: normal;
    color: var(--ink-grey);
    font-size: 14px;
    line-height: 18px;
  }
  .contact-list {
    position: absolute;
    left: 34px;
    top: 240px;
    list-style: none;
    color: var(--ink-grey);
    font-size: 14px;
  }
  .contact-list li {
    display: flex;
    align-items: center;
    gap: 10px;
    height: 22px;
  }
  .contact-icon { width: 15px; height: 15px; flex: none; }
</style>
</head>
<body>
  <section class="card card--front" aria-label="Card front">
    <span class="wordmark">velmora holdings</span>
  </section>

  <section class="card card--back" aria-label="Card back">
    <span class="wordmark">velmora holdings</span>
    <span class="holder-tab"></span>
    <h1 class="holder-name">Luis R. Albarda</h1>
    <address class="company-address">
      Velmora Holdings S.L.<br>
      Casa de Valdetorres Calle de Ortuzar<br>
      Beltrán 27, 28019 Madrid
    </address>
    <ul class="contact-list">
      <li>
        <svg class="contact-icon" viewBox="0 0 16 16" aria-hidden="true">
          <circle cx="8" cy="8" r="8" fill="#2b2c6e"/>
          <path d="M4.5 6.5c0-1 1.5-2 3.5-2s3.5 1 3.5 2l-1.2.6-.8-1.1H6.5l-.8 1.1z M5.5 8h5l.8 3.5H4.7z" fill="#fff"/>
        </svg>
        +34 (91) 387-6051
      </li>
      <li>
        <svg class="contact-icon" viewBox="0 0 16 16" aria-hidden="true">
          <circle cx="8" cy="8" r="8" fill="#2b2c6e"/>
          <rect x="5.5" y="3.5" width="5" height="9" rx="0.8" fill="#fff"/>
          <rect x="6.3" y="4.6" width="3.4" height="5" fill="#2b2c6e"/>
        </svg>
        +34 (655) 814-073
      </li>
      <li>
        <svg class="contact-icon" viewBox="0 0 16 16" aria-hidden="true">
          <circle cx="8" cy="8" r="8" fill="#2b2c6e"/>
          <text x="8" y="11.3" text-anchor="middle" font-size="10" fill="#fff" font-family="Arial, sans-serif">@</text>
        </svg>
        lalbarda@velmoraholdings.example
      </li>
    </ul>
  </section>
</body>
</html>
```